Orrowind Partners Business Card

Looking for a design for our business cards. Need to look corporate and outstanding. I have enclosed our logos for the company. Orrowind partners is an investment firm for high level clients looking for advisory in their investments. White background or black is good. We will like to double sided options maybe at the back with just the logo of the firm.

Example of the info for the business card:

Edric Salvo
Managing Director

Panama Phone +507 384 7165
Switzerland Phone +41 44 917 2638
mail@orrowind-partners.example
www.orrowind-partners.example

Industry/Entity Type

Investment

```html
<!DOCTYPE html>
<html lang="en">
<head>
<meta charset="utf-8">
<title>Orrowind Partners Business Card</title>
<link rel="stylesheet" href="https://fonts.googleapis.com/css2?family=Open+Sans:wght@400;600;700&display=swap">
<style>
  :root {
    --stage: #9a9a9a;
    --card-white: #ffffff;
    --card-dark: #333333;
    --navy: #1f3a82;
    --ink: #1a1a1a;
    --link-blue: #2a4a9a;
    --slate-block: #b8c3d8;
    --sand-block: #e9dcc0;
    --rule: #222222;
    --silver: #c9c9c9;
  }
  * { box-sizing: border-box; margin: 0; padding: 0; }
  html, body { width: 720px; height: 1200px; overflow: hidden; }
  body {
    background: var(--stage);
    font-family: "Open Sans", Arial, sans-serif;
    position: relative;
  }
  .card {
    position: absolute;
    left: 60px;
    width: 600px;
    height: 343px;
    overflow: hidden;
    box-shadow: 0 6px 18px rgba(0,0,0,0.35);
  }
  .card-front { top: 150px; background: var(--card-white); }
  .card-back { top: 700px; background: var(--card-dark); }

  .brand {
    position: absolute;
    display: flex;
    align-items: center;
    gap: 12px;
  }
  .brand-mark { width: 26px; height: 26px; }
  .brand-name {
    font-weight: 700;
    letter-spacing: 0.06em;
    text-transform: uppercase;
  }
  .card-front .brand { left: 36px; top: 38px; }
  .card-front .brand-mark { background: var(--navy); }
  .card-front .brand-name { color: var(--navy); font-size: 26px; }

  .accent-column { position: absolute; right: 0; top: 0; width: 132px; height: 100%; }
  .accent-block { position: absolute; left: 0; right: 0; }
  .accent-block.slate-top { top: 0; height: 112px; background: var(--slate-block); }
  .accent-block.slate-mid { top: 126px; height: 108px; background: var(--slate-block); }
  .accent-block.sand-base { top: 248px; bottom: 0; background: var(--sand-block); }

  .contact {
    position: absolute;
    right: 160px;
    top: 138px;
    text-align: right;
    color: var(--ink);
  }
  .contact-name { font-size: 19px; font-weight: 700; }
  .contact-title { font-size: 15px; margin-bottom: 14px; }
  .contact-line { font-size: 12px; line-height: 1.45; }
  .contact-email { color: var(--link-blue); }

  .divider {
    position: absolute;
    left: 26px;
    right: 150px;
    top: 262px;
    border-top: 1px solid var(--rule);
  }
  .website {
    position: absolute;
    left: 150px;
    top: 282px;
    font-size: 12px;
    color: var(--ink);
  }

  .card-back .brand {
    left: 0; right: 0; top: 0; bottom: 0;
    justify-content: center;
  }
  .card-back .brand-mark { background: var(--silver); width: 34px; height: 34px; }
  .card-back .brand-name { color: var(--silver); font-size: 32px; }
</style>
</head>
<body>
  <section class="card card-front" aria-label="Business card front">
    <div class="brand">
      <span class="brand-mark"></span>
      <span class="brand-name">Orrowind Partners</span>
    </div>
    <div class="accent-column">
      <div class="accent-block slate-top"></div>
      <div class="accent-block slate-mid"></div>
      <div class="accent-block sand-base"></div>
    </div>
    <div class="contact">
      <p class="contact-name">Edric Salvo</p>
      <p class="contact-title">Managing Director</p>
      <p class="contact-line contact-email">mail@orrowind-partners.example</p>
      <p class="contact-line">Panama Phone +507 384 7165</p>
      <p class="contact-line">Switzerland Phone +41 44 917 2638</p>
    </div>
    <div class="divider"></div>
    <p class="website">www.orrowind-partners.example</p>
  </section>

  <section class="card card-back" aria-label="Business card back">
    <div class="brand">
      <span class="brand-mark"></span>
      <span class="brand-name">Orrowind Partners</span>
    </div>
  </section>
</body>
</html>
```